Harborline Safety Courses

I'm currently in the process of setting up a First Aid and Lifeguard Training website. The project has already began through a web designer but he is unable to meet the deadline.
There's is already a landing page
http://www.harborlinesafetycourses.example.au/
In addition he also started to create the website
https://mockups.example.net/view/9c41d7e0-5b2a-4e8f-a613-d02e7bb18c39-2218/?fullscreen
The home page ideally needs to have a different visual and user journey from the quick landing page created
- The Logo in the top left hand corner looks a bit out of whack, maybe it needs to be bigger ??
-The tabs along the top need to be 'designed' and spaced out equally: home, about, courses, contact, gallery. Can we please remove Accredited First Aid and Lifeguard.
-the blue bar with the tag line needs to be redesigned - that was ok for a landing page but not quite right for actual website, it looks clunky
-all the course info needs to be placed under the courses tab not on the home page. I would like a roll down bar ( Check out Tidewater Rescue Aid website on their First Aid Course) so the client can book a date and proceed to the checkout basket. I will supply those soon; this will only apply to the Provide First Aid and Provide Cardiopulmonary Resuscitation Courses.
- The rest of the courses can have an enquire option
-the about paragraphs need to go directly under banner
-then a rolling slider with upcoming courses - with each course, rolling to give the home page some pop
- followed by pictures/ images of recent courses linked to gallery page updates or social feed
-remove newsletter
In addition to this I also have a logo designed via sketch harbor and lots of photos as well as briefs on all the courses that I will offer.
Accredited First Aid and CPR Courses. Lifeguard and Community Safety Programs Programs

```html
<!DOCTYPE html>
<html lang="en">
<head>
<meta charset="utf-8">
<title>Harborline Safety Courses</title>
<link href="https://fonts.googleapis.com/css2?family=Lato:wght@400;700;900&display=swap" rel="stylesheet">
<style>
:root{
  --navy:#062b48;
  --navy-deep:#04223a;
  --blue:#2c9ad3;
  --blue-bright:#1f8fd0;
  --orange:#f7931e;
  --white:#ffffff;
  --grey:#eeeeee;
  --text-grey:#666666;
}
*{margin:0;padding:0;box-sizing:border-box}
html,body{width:1200px;height:3943px;overflow:hidden}
body{position:relative;background:var(--navy);font-family:'Lato',sans-serif;color:var(--white)}
.abs{position:absolute}
.band{position:absolute;left:0;width:1200px}
.topbar{top:0;height:41px;background:var(--orange);text-align:center;font-size:13px;line-height:41px;color:var(--white)}
.topbar u{color:var(--navy)}
.hero{top:41px;height:495px;background:linear-gradient(180deg,#1d4461 0%,#2a4d66 50%,#264860 100%)}
.hero-photo{position:absolute;inset:0;background:linear-gradient(135deg,rgba(44,154,211,.35),rgba(6,43,72,.55))}
.brand{position:absolute;left:89px;top:61px;display:flex;align-items:center;gap:12px}
.brand-mark{width:22px;height:22px;border-radius:50%;background:var(--orange)}
.brand-name{font-size:17px;font-weight:700;color:var(--white);width:130px;line-height:1.2}
.nav{position:absolute;top:72px;left:528px;display:flex;gap:28px;font-size:14px}
.nav a{color:var(--white);text-decoration:none}
.nav a.active{color:var(--orange);text-decoration:underline}
.nav-icons{position:absolute;left:930px;top:72px;display:flex;gap:16px}
.login{position:absolute;left:1029px;top:67px;width:83px;height:35px;background:var(--orange);border-radius:3px;font-weight:700;font-size:14px;text-align:center;line-height:35px}
.hero h1{position:absolute;top:236px;left:0;width:1200px;text-align:center;font-size:34px;font-weight:900;line-height:36px}
.btn-outline{position:absolute;border:2px solid var(--white);border-radius:3px;text-align:center;font-size:14px;color:var(--white)}
.about h2,.section-title{font-size:32px;font-weight:900}
.about-copy{position:absolute;left:89px;top:665px;width:500px;font-size:13px;line-height:19px}
.about-copy p{margin-bottom:19px}
.about-photo{position:absolute;left:693px;top:597px;width:371px;height:347px;border-radius:24px 24px 24px 24px;background:linear-gradient(135deg,#c98a4a,#3aa7d8 60%,#2a4e80)}
.about-frame{position:absolute;left:705px;top:609px;width:367px;height:345px;border-radius:24px;border:5px solid var(--blue-bright);border-left:none;border-top:none}
.section-title{position:absolute;left:0;width:1200px;text-align:center}
.card{position:absolute;top:1185px;width:323px;height:477px;background:var(--white);border-radius:18px;overflow:hidden;color:#333}
.card-photo{height:173px}
.card h3{position:absolute;left:20px;top:193px;width:290px;color:var(--orange);font-size:17px;font-weight:700;line-height:22px}
.card table{position:absolute;left:19px;top:249px;width:285px;border-collapse:collapse;font-size:12px}
.card th{background:var(--blue);color:var(--white);font-weight:400;text-align:left;padding:0 16px;height:29px;border-radius:0}
.card td{background:var(--grey);height:31px;padding:0 16px;color:#111}
.card th:first-child{border-radius:6px 0 0 0}.card th:last-child{border-radius:0 6px 0 0;border-left:2px solid var(--white)}
.card td:last-child{border-left:2px solid var(--white)}
.card p{position:absolute;left:23px;top:340px;width:280px;font-size:12.5px;line-height:20px;color:var(--text-grey)}
.card .learn{position:absolute;left:23px;top:410px;width:122px;height:35px;border:2px solid var(--blue);color:var(--blue);border-radius:3px;text-align:center;line-height:31px;font-size:14px}
.card .book{position:absolute;left:153px;top:410px;width:122px;height:35px;background:var(--orange);color:var(--white);border-radius:3px;text-align:center;line-height:35px;font-size:14px}
.testimonial{position:absolute;top:2035px;left:230px;width:740px;text-align:center;font-size:13px;line-height:20px}
.author{position:absolute;top:2107px;left:0;width:1200px;text-align:center;font-size:13px}
.author span{color:var(--orange)}
.author small{font-size:11px}
.gphoto{position:absolute;width:323px;height:204px;border-radius:16px}
.field{position:absolute;border:1px solid #4f6c86;font-size:12px;color:#c9d4de;padding:11px 0 0 32px}
.field svg{position:absolute;left:10px;top:10px}
.submit{position:absolute;left:545px;top:3427px;width:110px;height:38px;background:var(--orange);border-radius:3px;text-align:center;line-height:38px;font-weight:700;font-size:14px}
.footer-bg{top:3566px;height:334px;background:linear-gradient(180deg,#0b2a42,#123652)}
.foot-h{position:absolute;top:3644px;color:var(--orange);font-size:18px;font-weight:700}
.foot-links{position:absolute;left:328px;top:3690px;list-style:none;font-size:14px;line-height:31px}
.contact{position:absolute;left:471px;font-size:14px;line-height:19px;display:flex;gap:14px}
.contact svg{flex:none;margin-top:2px}
.map{position:absolute;left:800px;top:3653px;width:311px;height:174px;background:linear-gradient(135deg,#f2f2ef,#dfe6ea)}
.bottombar{top:3900px;height:43px;background:var(--orange);font-size:13px;line-height:43px;padding-left:89px}
.social{position:absolute;top:3915px;display:flex;gap:18px;left:1004px}
.social i{display:block;width:13px;height:13px;border-radius:50%;background:var(--white)}
</style>
</head>
<body>

<div class="band topbar">We are open for business: Please View our <u>Covid Guidelines</u></div>

<header class="band hero">
  <div class="hero-photo" role="img" aria-label="Photo of lifeguard trainees in team shirts on the beach with rescue vehicles"></div>
</header>

<div class="brand"><span class="brand-mark"></span><span class="brand-name">Harborline Safety Courses</span></div>
<nav class="nav">
  <a class="active">Home</a><a>About Us</a><a>Courses</a><a>Gallery</a><a>Contact Us</a>
</nav>
<div class="nav-icons">
  <svg width="20" height="20" viewBox="0 0 20 20" fill="none" stroke="#fff" stroke-width="2"><circle cx="8" cy="8" r="6"/><path d="M13 13l5 5"/></svg>
  <svg width="24" height="20" viewBox="0 0 24 20" fill="none" stroke="#fff" stroke-width="2"><path d="M1 2h4l3 11h12l3-8H7"/><circle cx="10" cy="17" r="1.5"/><circle cx="19" cy="17" r="1.5"/></svg>
</div>
<div class="login">Login</div>

<h1 class="hero abs" style="background:none;height:auto"></h1>
<div class="abs" style="top:236px;left:0;width:1200px;text-align:center;font-size:34px;font-weight:900;line-height:36px">Accredited training from first aid<br>to lifeguard programs</div>
<div class="btn-outline" style="left:523px;top:332px;width:138px;height:37px;line-height:33px">Learn More</div>

<!-- hero base shape -->
<svg class="abs" style="left:0;top:430px" width="1200" height="110" viewBox="0 0 1200 110">
  <polygon points="0,10 600,80 1200,10 1200,110 0,110" fill="var(--navy)"/>
  <polygon points="190,42 600,95 1010,42 600,104" fill="var(--orange)"/>
  <polygon points="0,10 600,80 1200,10 1200,14 600,86 0,14" fill="var(--navy)"/>
</svg>

<!-- About -->
<section class="about">
  <h2 class="abs" style="left:89px;top:597px">About Us</h2>
  <div class="about-copy">
    <p><b>Harborline Safety Courses delivers a series of Emergency training accreditation and innovative general safety awareness programs.</b></p>
    <p>From general first aid to Lifeguard training courses, our carefully designed training methods ensure all students leave with clarity and confidence in managing emergency scenarios.</p>
    <p>We ensure our training programs are facilitated in a way that enhances learning through shared practical knowledge and shared relatable experiences. Corey Daleman, founder has over 25 years' experience...</p>
  </div>
  <div class="btn-outline" style="left:89px;top:894px;width:138px;height:38px;line-height:34px">Learn More</div>
  <div class="about-frame"></div>
  <div class="about-photo" role="img" aria-label="Photo of the founder in a lifeguard shirt teaching a class"></div>
</section>

<!-- Courses band -->
<svg class="abs" style="left:0;top:1015px" width="1200" height="811" viewBox="0 0 1200 811">
  <polygon points="0,80 600,0 1200,80 1200,734 600,811 0,734" fill="var(--blue)"/>
</svg>
<div class="section-title" style="top:1113px">Accredited Courses Available</div>

<article class="card" style="left:89px">
  <div class="card-photo" role="img" aria-label="Photo of trainees practising CPR on a manikin at the beach" style="background:linear-gradient(180deg,#7fb3d6 0%,#d8c4a0 45%,#c9a27a 100%)"></div>
  <h3>Provide Cardiopulmonary Resuscitation</h3>
  <table><tr><th>Course ID</th><th>Cost:</th></tr><tr><td>HLTAID009</td><td>$45.00</td></tr></table>
  <p>This unit describes the skills and knowledge required to perform cardiopulmonary resuscitation (CPR) in line with the...</p>
  <div class="learn">Learn More</div><div class="book">Book Now</div>
</article>
<article class="card" style="left:438px">
  <div class="card-photo" role="img" aria-label="Photo of a group practising resuscitation in a training pool area" style="background:linear-gradient(180deg,#1e3f6a,#3b78b5 60%,#9fc6e2)"></div>
  <h3>Provide Advanced Resuscitation and Oxygen Therapy</h3>
  <table><tr><th>Course ID</th><th>Cost:</th></tr><tr><td>HLTAID015</td><td>$130.00</td></tr></table>
  <p>This course will provide you with the skills and knowledge required to use specialised equipment in the provision of...</p>
  <div class="learn">Learn More</div><div class="book">Book Now</div>
</article>
<article class="card" style="left:787px">
  <div class="card-photo" role="img" aria-label="Photo of students kneeling around a first aid manikin on sand" style="background:linear-gradient(180deg,#e8e4dc,#c9b48e 60%,#a88560)"></div>
  <h3 style="top:203px">Provide Advanced First Aid</h3>
  <table><tr><th>Course ID</th><th>Cost:</th></tr><tr><td>HLTAID014</td><td>$150.00</td></tr></table>
  <p>This course supersedes HLTAID006 Provide Advanced First Aid, this unit describes the skills and knowledge required to perform...</p>
  <div class="learn">Learn More</div><div class="book">Book Now</div>
</article>

<svg class="abs" style="left:570px;top:1713px" width="60" height="26" viewBox="0 0 60 26">
  <circle cx="12" cy="13" r="12" fill="#7fbde3"/><path d="M16 13H8m3-4l-4 4 4 4" stroke="var(--blue)" stroke-width="2" fill="none"/>
  <circle cx="47" cy="13" r="12" fill="#fff"/><path d="M43 13h8m-3-4l4 4-4 4" stroke="var(--blue)" stroke-width="2" fill="none"/>
</svg>

<!-- Testimonials -->
<div class="abs" role="img" aria-label="Faded photo of course participants in the background" style="left:0;top:1780px;width:1200px;height:520px;background:linear-gradient(180deg,rgba(255,255,255,.04),rgba(255,255,255,.08))"></div>
<div class="section-title" style="top:1898px">Testimonials</div>
<svg class="abs" style="left:575px;top:1963px" width="50" height="50" viewBox="0 0 50 50">
  <circle cx="25" cy="25" r="25" fill="var(--orange)"/>
  <path d="M14 30c0-6 3-10 8-11v4c-2 1-3 2-3 4h3v7h-8zM27 30c0-6 3-10 8-11v4c-2 1-3 2-3 4h3v7h-8z" fill="#fff"/>
</svg>
<p class="testimonial">Lorem Ipsum is simply dummy text of the printing and typesetting industry. Lorem Ipsum has been the industry's standard dummy text ever since the 1500s, when an unknown printer took a galley of type and scrambled it to make a type specimen book. It has survived not only five centuries, but also the leap into...</p>
<div class="author"><span>Marla Penrose</span> <small>Simply Beautiful</small></div>
<svg class="abs" style="left:129px;top:2050px" width="26" height="26" viewBox="0 0 26 26"><rect x="1" y="1" width="24" height="24" rx="7" fill="none" stroke="#6f8aa0" stroke-width="2"/><path d="M17 13H9m3-4l-4 4 4 4" stroke="#6f8aa0" stroke-width="2" fill="none"/></svg>
<svg class="abs" style="left:1046px;top:2050px" width="26" height="26" viewBox="0 0 26 26"><rect x="1" y="1" width="24" height="24" rx="7" fill="none" stroke="#fff" stroke-width="2"/><path d="M9 13h8m-3-4l4 4-4 4" stroke="#fff" stroke-width="2" fill="none"/></svg>
<div class="btn-outline" style="left:531px;top:2166px;width:136px;height:38px;line-height:34px">Learn More</div>

<!-- Gallery band -->
<svg class="abs" style="left:0;top:2278px" width="1200" height="730" viewBox="0 0 1200 730">
  <polygon points="0,79 600,0 1200,79 1200,725 0,725" fill="var(--blue)"/>
</svg>
<div class="section-title" style="top:2375px">Gallery</div>
<div class="gphoto" style="left:89px;top:2449px;background:linear-gradient(180deg,#7fb3d6,#d8c4a0 45%,#c9a27a)" role="img" aria-label="Photo of CPR training on the beach"></div>
<div class="gphoto" style="left:438px;top:2449px;background:linear-gradient(180deg,#2f6fa8,#5aa6d8 55%,#bcd9ec)" role="img" aria-label="Photo of a stretcher rescue drill in a pool area"></div>
<div class="gphoto" style="left:787px;top:2449px;background:linear-gradient(180deg,#e8e4dc,#c9b48e 60%,#a88560)" role="img" aria-label="Photo of students practising first aid on sand"></div>
<div class="gphoto" style="left:89px;top:2680px;background:linear-gradient(135deg,#2a5d9a,#7fa6c7 50%,#3a4a66)" role="img" aria-label="Photo of a lifeguard beside a rescue jet ski"></div>
<div class="gphoto" style="left:438px;top:2680px;background:linear-gradient(180deg,#5f7ea8,#b8d34a 55%,#6a6a5a)" role="img" aria-label="Group photo of trainees in hi-vis vests with manikins"></div>
<div class="gphoto" style="left:787px;top:2680px;background:linear-gradient(180deg,#6fa4d6,#2f8fc7 55%,#d6c7aa)" role="img" aria-label="Photo of instructors with rescue gear on the beach"></div>
<div class="btn-outline" style="left:531px;top:2936px;width:137px;height:38px;line-height:34px">Learn More</div>

<!-- Quick Inquiry -->
<div class="section-title" style="top:3155px">Quick Inquiry</div>
<div class="field" style="left:126px;top:3227px;width:304px;height:36px"><svg width="14" height="14" viewBox="0 0 14 14" fill="none" stroke="var(--blue)" stroke-width="1.5"><circle cx="7" cy="4" r="3"/><path d="M1 13c1-4 11-4 12 0"/></svg>Name</div>
<div class="field" style="left:447px;top:3227px;width:305px;height:36px"><svg width="14" height="14" viewBox="0 0 14 14" fill="none" stroke="var(--blue)" stroke-width="1.5"><rect x="1" y="3" width="12" height="9"/><path d="M1 3l6 5 6-5"/></svg>Email</div>
<div class="field" style="left:768px;top:3227px;width:305px;height:36px"><svg width="14" height="14" viewBox="0 0 14 14" fill="none" stroke="var(--blue)" stroke-width="1.5"><rect x="3" y="1" width="8" height="12" rx="1"/></svg>Phone</div>
<div class="field" style="left:126px;top:3280px;width:947px;height:104px"><svg width="14" height="14" viewBox="0 0 14 14" fill="none" stroke="var(--blue)" stroke-width="1.5"><rect x="1" y="1" width="12" height="12" rx="2"/><path d="M4 10l6-6"/></svg>How can we help?</div>
<div class="submit">Submit</div>

<!-- Footer -->
<svg class="abs" style="left:0;top:3540px" width="1200" height="70" viewBox="0 0 1200 70"><polygon points="0,50 600,20 1200,50 1200,70 0,70" fill="#0b2a42"/></svg>
<div class="band footer-bg" role="img" aria-label="Dark faded photo of a training group"></div>
<div class="abs" style="left:89px;top:3725px;display:flex;align-items:center;gap:10px">
  <span style="width:20px;height:20px;border-radius:50%;background:var(--orange)"></span>
  <span style="font-size:16px;font-weight:700;width:118px;line-height:1.2">Harborline Safety Courses</span>
</div>
<div class="foot-h" style="left:328px">Quick Link</div>
<ul class="foot-links"><li>Home</li><li>About Us</li><li>Courses</li><li>Gallery</li><li>Contact Us</li></ul>
<div class="foot-h" style="left:471px">Contact info</div>
<div class="contact" style="top:3689px"><svg width="16" height="18" viewBox="0 0 16 18"><path d="M8 1a6 6 0 0 1 6 6c0 4-6 10-6 10S2 11 2 7a6 6 0 0 1 6-6z" fill="var(--orange)"/><circle cx="8" cy="7" r="2" fill="#0b2a42"/></svg><span>ABN 41 309 552 187<br>Office 3/12 Bluegum Lane, Seacliff,<br>NSW, 2590</span></div>
<div class="contact" style="top:3757px"><svg width="16" height="16" viewBox="0 0 16 16"><path d="M3 1l3 3-2 2c1 3 3 5 6 6l2-2 3 3-2 2C7 15 1 9 1 3z" fill="var(--orange)"/></svg><span>0400 555 218</span></div>
<div class="contact" style="top:3786px"><svg width="16" height="16" viewBox="0 0 16 16"><rect x="1" y="3" width="14" height="10" fill="var(--orange)"/><path d="M1 3l7 6 7-6" stroke="#0b2a42" fill="none"/></svg><span style="font-size:13px">corey@harborlinesafetycourses.example.au</span></div>
<div class="contact" style="top:3816px"><svg width="16" height="16" viewBox="0 0 16 16"><circle cx="8" cy="8" r="7" fill="var(--orange)"/><path d="M8 4v4l3 2" stroke="#0b2a42" stroke-width="1.5" fill="none"/></svg><span>9am-5pm</span></div>
<div class="map" role="img" aria-label="Street map showing the office location"></div>

<div class="band bottombar">Copyright © 2021 Harborline Safety Courses. All Rights Reserved</div>
<div class="social"><i></i><i></i><i></i><i></i></div>

</body>
</html>
```